Commercial Construction Company

We need a business card design based on our current logo. We are a commercial general contractor based in Southern California that specializes in bank remodels. We would like to see designs that incorporate dark blue. The final design should portray an image of professionalism and quality.

If possible, I would like to add metallic foil to the design. Thank you

```html
<!DOCTYPE html>
<html lang="en">
<head>
<meta charset="utf-8">
<title>Kestrel Builders – Business Card</title>
<link href="https://fonts.googleapis.com/css2?family=Quicksand:wght@400;500;700&display=swap" rel="stylesheet">
<style>
  :root {
    --navy: #172649;
    --navy-deep: #111d3a;
    --grey-text: #7a7c80;
    --rule: #8e9094;
    --paper: #f4f4f3;
    --backdrop: #e8e8e8;
  }
  html, body {
    margin: 0;
    padding: 0;
    width: 1200px;
    height: 1200px;
    overflow: hidden;
    background: var(--backdrop);
    font-family: "Quicksand", sans-serif;
  }
  .card {
    position: absolute;
    left: 227px;
    width: 745px;
    height: 425px;
    box-sizing: border-box;
  }
  .card-front { top: 135px; background: var(--paper); }
  .card-back { top: 639px; background: var(--navy); }

  .brand-lockup {
    position: absolute;
    left: 40px;
    top: 178px;
    width: 300px;
    display: flex;
    align-items: center;
    gap: 12px;
  }
  .brand-mark {
    width: 22px;
    height: 22px;
    border-radius: 50%;
    background: var(--navy);
    flex: none;
  }
  .brand-name {
    font-weight: 700;
    font-size: 38px;
    letter-spacing: 1px;
    color: var(--navy);
    line-height: 1;
  }

  .divider {
    position: absolute;
    left: 373px;
    top: 77px;
    width: 1px;
    height: 271px;
    background: var(--rule);
  }

  .contact-block {
    position: absolute;
    left: 414px;
    top: 76px;
    color: var(--grey-text);
    font-size: 17px;
    letter-spacing: 1.3px;
  }
  .person-name {
    margin: 0;
    font-weight: 700;
    font-size: 22px;
    letter-spacing: 2.2px;
    color: var(--navy);
    line-height: 1.3;
  }
  .person-title { margin: 2px 0 0; line-height: 1.3; }
  .address { margin: 30px 0 0; line-height: 24px; font-style: normal; }
  .contact-list { list-style: none; margin: 32px 0 0; padding: 0; }
  .contact-list li {
    display: flex;
    align-items: center;
    gap: 10px;
    height: 24px;
  }
  .contact-icon { width: 18px; height: 18px; flex: none; }
  .web strong { color: var(--navy); font-weight: 700; }

  .back-name {
    position: absolute;
    left: 0;
    right: 0;
    top: 186px;
    text-align: center;
    font-weight: 700;
    font-size: 46px;
    letter-spacing: 1.5px;
    color: var(--navy-deep);
    line-height: 1;
  }
</style>
</head>
<body>

<section class="card card-front">
  <div class="brand-lockup">
    <span class="brand-mark"></span>
    <span class="brand-name">KESTREL</span>
  </div>

  <div class="divider"></div>

  <div class="contact-block">
    <h1 class="person-name">MORGAN HALE</h1>
    <p class="person-title">CEO at Kestrel Builders Inc.</p>
    <address class="address">
      4120 Mesa Ridge Way<br>
      Suite 310<br>
      Ontario, CA 91761
    </address>
    <ul class="contact-list">
      <li>
        <svg class="contact-icon" viewBox="0 0 18 18" aria-hidden="true">
          <circle cx="9" cy="9" r="9" fill="var(--navy)"/>
          <path d="M4.5 7.5 Q9 3.5 13.5 7.5 L12.2 8.8 L10.8 7.6 L7.2 7.6 L5.8 8.8 Z" fill="#fff"/>
          <rect x="6" y="9" width="6" height="4" rx="1" fill="#fff"/>
        </svg>
        <span>(555) 214-0386</span>
      </li>
      <li>
        <svg class="contact-icon" viewBox="0 0 18 18" aria-hidden="true">
          <circle cx="9" cy="9" r="9" fill="var(--navy)"/>
          <rect x="5" y="4" width="6" height="4" fill="none" stroke="#fff" stroke-width="1.2"/>
          <rect x="4.5" y="8" width="9" height="6" rx="1" fill="#fff"/>
        </svg>
        <span>(555) 214-0391</span>
      </li>
      <li>
        <svg class="contact-icon" viewBox="0 0 18 18" aria-hidden="true">
          <circle cx="9" cy="9" r="9" fill="var(--navy)"/>
          <rect x="4.5" y="5.5" width="9" height="7" fill="none" stroke="#fff" stroke-width="1.2"/>
          <path d="M4.5 5.5 L9 9.5 L13.5 5.5" fill="none" stroke="#fff" stroke-width="1.2"/>
        </svg>
        <span>info@kestrelbuilds.com</span>
      </li>
      <li class="web">
        <svg class="contact-icon" viewBox="0 0 18 18" aria-hidden="true">
          <circle cx="9" cy="9" r="9" fill="var(--navy)"/>
          <circle cx="9" cy="9" r="5" fill="none" stroke="#fff" stroke-width="1.2"/>
          <path d="M4 9 H14 M9 4 Q6 9 9 14 M9 4 Q12 9 9 14" fill="none" stroke="#fff" stroke-width="1"/>
        </svg>
        <span>www.<strong>kestrelbuilds</strong>.com</span>
      </li>
    </ul>
  </div>
</section>

<section class="card card-back">
  <div class="back-name">KESTREL</div>
</section>

</body>
</html>
```